Ember needs a new design we have an updated logo and want a high qualitative high end feel

feel and aesthetic should be high qualitative like the packaging in a zelvo or the qualatative weight/feel of an zelvo design. modern, elegant bold.probably just the ember logo on the backone vesion could be blue background white letter ... open to ideas
legal, insurance , medical, finance vantor 300
Information Technology
Serif

```html
<!DOCTYPE html>
<html lang="en">
<head>
<meta charset="utf-8">
<title>Ember Managed Services Group – Business Cards</title>
<link rel="stylesheet" href="https://fonts.googleapis.com/css2?family=Montserrat:wght@500;600;700&family=Lato:wght@400;700&display=swap">
<style>
  :root {
    --navy: #1b2d45;
    --paper: #fcf8f8;
    --ink: #1d2a3b;
    --divider: #c9c9cf;
    --stage: #e6e6e8;
  }
  * { box-sizing: border-box; margin: 0; padding: 0; }
  html, body { width: 1200px; height: 782px; overflow: hidden; }
  body {
    background: var(--stage);
    position: relative;
    font-family: "Lato", Arial, sans-serif;
    color: var(--ink);
  }
  .card {
    position: absolute;
    top: 236px;
    width: 540px;
    height: 309px;
    overflow: hidden;
    box-shadow: 0 6px 18px rgba(0,0,0,0.18);
  }
  .card--front { left: 40px; background: var(--paper); }
  .card--back { left: 620px; background: var(--navy); }

  .wave { position: absolute; inset: 0; width: 100%; height: 100%; }

  .brand {
    position: absolute;
    left: 26px;
    top: 72px;
    width: 262px;
    display: flex;
    align-items: flex-end;
    gap: 8px;
  }
  .brand__name {
    font-family: "Montserrat", Arial, sans-serif;
    font-weight: 600;
    font-size: 52px;
    line-height: 0.9;
    letter-spacing: 0.5px;
    color: var(--navy);
    white-space: nowrap;
  }
  .brand__tagline {
    font-family: "Montserrat", Arial, sans-serif;
    font-weight: 600;
    font-size: 8px;
    line-height: 1.25;
    letter-spacing: 0.2px;
    color: var(--navy);
    text-transform: uppercase;
    white-space: nowrap;
    padding-bottom: 2px;
  }

  .divider {
    position: absolute;
    left: 300px;
    top: 58px;
    width: 1px;
    height: 120px;
    background: linear-gradient(to bottom, transparent, var(--divider) 25%, var(--divider) 75%, transparent);
  }

  .contact {
    position: absolute;
    left: 316px;
    top: 56px;
    width: 214px;
  }
  .contact__name {
    font-family: "Montserrat", Arial, sans-serif;
    font-weight: 700;
    font-size: 20px;
    line-height: 1.05;
    color: var(--ink);
  }
  .contact__title {
    font-size: 14px;
    line-height: 1.3;
    margin-bottom: 6px;
  }
  .contact__line {
    display: flex;
    align-items: center;
    gap: 6px;
    font-size: 14px;
    line-height: 1.35;
  }
  .contact__line svg { width: 12px; height: 12px; fill: var(--ink); flex: none; }
  .contact__company {
    font-weight: 700;
    font-size: 14px;
    line-height: 1.3;
    margin-top: 6px;
  }
  .contact__address { font-size: 14px; line-height: 1.3; }

  .back-mark {
    position: absolute;
    left: 345px;
    top: 172px;
    font-family: "Montserrat", Arial, sans-serif;
    font-weight: 600;
    font-size: 26px;
    letter-spacing: 0.5px;
    color: #ffffff;
  }
</style>
</head>
<body>

  <section class="card card--front" aria-label="Business card front">
    <svg class="wave" viewBox="0 0 540 309" preserveAspectRatio="none" aria-hidden="true">
      <path d="M0,150 C110,148 190,210 320,250 C420,280 490,282 540,276 L540,309 L0,309 Z" fill="var(--navy)"/>
      <path d="M0,160 C110,158 190,220 320,260 C420,290 490,292 540,286" fill="none" stroke="#ffffff" stroke-width="2"/>
    </svg>

    <div class="brand">
      <span class="brand__name">ember</span>
      <span class="brand__tagline">Managed<br>Services<br>Group, Inc.</span>
    </div>

    <div class="divider"></div>

    <div class="contact">
      <p class="contact__name">Daniel Hart</p>
      <p class="contact__title">Managing Director</p>
      <p class="contact__line">
        <svg viewBox="0 0 24 24" aria-hidden="true"><path d="M6.6 10.8a15.1 15.1 0 0 0 6.6 6.6l2.2-2.2a1 1 0 0 1 1-.25 11.4 11.4 0 0 0 3.6.57 1 1 0 0 1 1 1V20a1 1 0 0 1-1 1A17 17 0 0 1 3 4a1 1 0 0 1 1-1h3.5a1 1 0 0 1 1 1c0 1.25.2 2.45.57 3.57a1 1 0 0 1-.25 1z"/></svg>
        (555) 214-7730
      </p>
      <p class="contact__line">
        <svg viewBox="0 0 24 24" aria-hidden="true"><path d="M2 5h20v14H2z M3.5 6.5 12 13l8.5-6.5" fill="var(--ink)" stroke="var(--paper)" stroke-width="1.4"/></svg>
        help@embermsg.com
      </p>
      <p class="contact__company">Ember Managed Services<br>Group, Inc.</p>
      <p class="contact__address">482 Linden Ave Suite 310<br>Fairhaven, VA 23100</p>
    </div>
  </section>

  <section class="card card--back" aria-label="Business card back">
    <span class="back-mark">ember</span>
  </section>

</body>
</html>
```